Corwin Crest Homes Needs Business Card Design

Looking for a unique modern business card to fit my new Logo.
Name: Marcus Corwin
Company: Corwin Crest Homes, LLC
Tag Line: Crafted To Last
Email: corwincresthomes@mailnest.example
Phone: (555) 017-2846
Website: www.corwincresthomes.example
License: CORWICH462KX

```html
<!DOCTYPE html>
<html lang="en">
<head>
<meta charset="utf-8">
<title>Corwin Crest Homes – Business Card</title>
<link href="https://fonts.googleapis.com/css2?family=Montserrat:wght@400;500;600;700&display=swap" rel="stylesheet">
<style>
  :root {
    --brand-blue: #3698cb;
    --ink: #151515;
    --paper: #ffffff;
    --backdrop: #d4d5d7;
  }
  * { margin: 0; padding: 0; box-sizing: border-box; }
  html, body {
    width: 900px; height: 1200px; overflow: hidden;
    background: var(--backdrop);
    font-family: "Montserrat", sans-serif;
  }
  .canvas { position: relative; width: 900px; height: 1200px; }

  .card { position: absolute; left: 118px; width: 664px; height: 380px; }

  /* Front */
  .card-front { top: 200px; background: var(--brand-blue); }
  .front-brand {
    position: absolute; left: 0; right: 0; top: 150px;
    display: flex; flex-direction: column; align-items: center; gap: 22px;
  }
  .front-brand .brand-mark { width: 56px; height: 56px; background: var(--paper); }
  .front-brand .brand-name {
    color: var(--paper); font-weight: 700; font-size: 34px; letter-spacing: 0.5px;
  }

  /* Back */
  .card-back { top: 616px; background: var(--paper); }
  .back-brand {
    position: absolute; left: 41px; top: 70px;
    display: flex; align-items: center; gap: 12px;
  }
  .back-brand .brand-mark { width: 34px; height: 34px; background: var(--brand-blue); }
  .back-brand .brand-name {
    color: var(--ink); font-weight: 700; font-size: 20px; letter-spacing: 0.2px;
  }

  .owner { position: absolute; right: 34px; top: 74px; text-align: right; }
  .owner-name {
    color: var(--brand-blue); font-weight: 600; font-size: 25px; letter-spacing: 1.5px;
    line-height: 1;
  }
  .owner-title { color: var(--ink); font-size: 14px; letter-spacing: 0.8px; margin-top: 8px; }

  .contacts { position: absolute; left: 40px; top: 247px; list-style: none; }
  .contacts li {
    display: flex; align-items: center; gap: 8px;
    color: var(--ink); font-size: 15px; letter-spacing: 0.6px; height: 24px;
  }
  .contacts li.phone { letter-spacing: 2.4px; }
  .contacts svg { width: 16px; height: 16px; flex: none; }
  .license {
    position: absolute; left: 40px; top: 329px;
    font-size: 15px; letter-spacing: 1px; color: var(--ink);
  }
  .license-label { color: var(--brand-blue); font-weight: 500; }

  .tagline {
    position: absolute; right: 0; top: 318px; width: 287px; height: 40px;
    background: var(--brand-blue); border-radius: 20px 0 0 20px;
    color: var(--paper); font-weight: 600; font-size: 17px; letter-spacing: 1.8px;
    display: flex; align-items: center; padding-left: 17px;
  }
</style>
</head>
<body>
<main class="canvas">

  <section class="card card-front">
    <div class="front-brand">
      <span class="brand-mark"></span>
      <span class="brand-name">Corwin Crest Homes</span>
    </div>
  </section>

  <section class="card card-back">
    <div class="back-brand">
      <span class="brand-mark"></span>
      <span class="brand-name">Corwin Crest Homes</span>
    </div>

    <div class="owner">
      <p class="owner-name">MARCUS CORWIN</p>
      <p class="owner-title">Owner</p>
    </div>

    <ul class="contacts">
      <li class="phone">
        <svg viewBox="0 0 16 16" aria-hidden="true"><path fill="#3698cb" d="M3.6 1.2l2.2 2.6-1.2 1.8c.9 2 2.3 3.4 4.3 4.4l1.8-1.2 2.6 2.2-1.4 2.3C6.5 13.1 2.8 9.4 1.4 3l2.2-1.8z"/></svg>
        (555) 017-2846
      </li>
      <li>
        <svg viewBox="0 0 16 16" aria-hidden="true"><rect x="1" y="3" width="14" height="10" fill="#3698cb"/><path d="M1.5 3.5L8 9l6.5-5.5" stroke="#fff" stroke-width="1.2" fill="none"/></svg>
        corwincresthomes@mailnest.example
      </li>
      <li>
        <svg viewBox="0 0 16 16" aria-hidden="true"><g fill="none" stroke="#3698cb" stroke-width="1.2"><circle cx="8" cy="8" r="6.5"/><ellipse cx="8" cy="8" rx="3" ry="6.5"/><path d="M1.5 8h13M2.5 5h11M2.5 11h11"/></g></svg>
        www.corwincresthomes.example
      </li>
    </ul>

    <p class="license"><span class="license-label">License:</span> CORWICH462KX</p>

    <div class="tagline">CRAFTED TO LAST</div>
  </section>

</main>
</body>
</html>
```